Escape Room Brochure, Trifold. Bold Black, yellow red. Doors Keys

We need a brochure to introduce our escape room and our services.
Attached are some of our designs as well as some examples of brochures we like.
We are THE VAULTS of KDW, however, we are aiming at Can you slip the vaults of KDW.
We are one of three escape rooms in a college town. We believe our rooms are more creative and original. Only family friendly. Brochure to be distributed to explain what an escape room is and promote our new fundraising program.

Font styles to use
Other font styles liked:
• impact

Colors
fbee3e
ec1f27
000000
dbdbdb

Requirements
Must have
• description of our rooms. services we offer. Fundraising and group teambuilding. Most information can be found at thevaultsofkdw.com
• what is an escape room.
Nice to have
• Photoshop
Should not have
• padlock or maze

```html
<!DOCTYPE html>
<html lang="en">
<head>
<meta charset="utf-8">
<title>The Vaults of KDW – Trifold Brochure</title>
<link rel="stylesheet" href="https://fonts.googleapis.com/css2?family=Anton&family=Mulish:wght@400;600;700&display=swap">
<style>
  :root {
    --yellow: #f2e43f;
    --red: #e4262b;
    --black: #1b1b1b;
    --ink: #161616;
    --white: #ffffff;
    --grey: #dbdbdb;
    --stage: #e9e9e9;
    --head: "Anton", Impact, sans-serif;
    --body: "Mulish", Arial, sans-serif;
  }
  * { box-sizing: border-box; margin: 0; padding: 0; }
  html, body { width: 1200px; height: 1000px; overflow: hidden; background: var(--stage); }
  .brochure {
    position: absolute; left: 57px; top: 50px; width: 1086px; height: 847px;
    overflow: hidden; font-family: var(--body); color: var(--white);
  }
  .backdrop { position: absolute; inset: 0; }
  .panel { position: absolute; top: 0; height: 100%; }
  .panel-left { left: 0; width: 363px; }
  .panel-middle { left: 363px; width: 367px; }
  .panel-right { left: 730px; width: 356px; }

  /* left panel */
  .about-title {
    position: absolute; left: 0; width: 380px; top: 92px; text-align: center;
    font-family: var(--head); font-size: 34px; color: var(--red); letter-spacing: 0.2px;
  }
  .keys-photo {
    position: absolute; left: 45px; top: 155px; width: 288px; height: 187px;
    border: 3px solid var(--white);
    background: radial-gradient(circle at 40% 45%, #9a9a9a, #4a4a4a 55%, #1e1e1e);
  }
  .about-text {
    position: absolute; left: 50px; top: 380px; width: 300px;
    font-size: 11.3px; line-height: 15.2px; color: var(--white);
  }
  .hours {
    position: absolute; left: 0; width: 370px; top: 546px; text-align: center;
    font-size: 13px; line-height: 16.5px;
  }
  .hours .hl { color: var(--yellow); font-weight: 600; }
  .divider { width: 205px; height: 1px; background: #777; margin: 16px auto 16px; }
  .closed { font-size: 11.5px; line-height: 15.5px; width: 250px; margin: 0 auto; }
  .closed .hl { font-weight: 400; }
  .sign-off {
    position: absolute; left: 0; width: 360px; top: 770px; text-align: center;
    font-size: 17px; line-height: 23px; color: var(--yellow); font-weight: 600;
  }

  /* middle panel */
  .brand-title {
    position: absolute; left: 0; width: 367px; top: 55px; text-align: center;
    font-family: var(--head); font-size: 58px; line-height: 64px; color: var(--ink);
  }
  .title-rule { position: absolute; left: 45px; width: 270px; top: 193px; height: 1.5px; background: var(--ink); }
  .tagline {
    position: absolute; left: 0; width: 360px; top: 198px; text-align: center;
    font-family: var(--head); font-size: 27px; color: var(--red);
  }
  .map-area {
    position: absolute; left: 35px; top: 264px; width: 285px; height: 202px;
    border: 3px solid var(--white);
    background: linear-gradient(135deg, #ececec, #dcdcdc 60%, #e8e4d0);
  }
  .address {
    position: absolute; left: 0; width: 360px; top: 480px; text-align: center;
    font-size: 14.5px; line-height: 18px; font-weight: 600; color: var(--ink);
  }
  .address svg { vertical-align: -1px; margin-right: 3px; }
  .wordmark {
    font-family: var(--head); color: var(--yellow); text-align: center; letter-spacing: 1px;
    display: flex; align-items: center; justify-content: center; gap: 10px;
  }
  .wordmark .mark { width: 14px; height: 14px; background: var(--yellow); }
  .wordmark-middle { position: absolute; left: 0; width: 360px; top: 640px; font-size: 26px; }
  .phone {
    position: absolute; left: 0; width: 360px; top: 716px; text-align: center; font-size: 21px;
  }
  .contact { text-align: center; font-size: 14px; line-height: 20px; }
  .contact svg { vertical-align: -1px; margin-right: 5px; }
  .contact-middle { position: absolute; left: 0; width: 360px; top: 750px; }

  /* right panel */
  .wordmark-right { position: absolute; left: 0; width: 356px; top: 168px; font-size: 30px; }
  .subtitle {
    position: absolute; left: 0; width: 356px; top: 255px; text-align: center;
    font-family: var(--head); font-size: 22px; color: var(--white); letter-spacing: 0.3px;
  }
  .contact-right { position: absolute; left: 0; width: 356px; top: 291px; font-size: 13.5px; line-height: 19px; }
  .door-photo {
    position: absolute; left: 0; top: 360px; width: 356px; height: 487px;
    background:
      radial-gradient(ellipse at 35% 70%, rgba(210,210,210,0.55), rgba(0,0,0,0) 55%),
      linear-gradient(180deg, #1b1b1b 0%, #2a2a2a 60%, #3c3c3c 100%);
  }
  .yellow { color: var(--yellow); }
</style>
</head>
<body>
<main class="brochure">
  <svg class="backdrop" width="1086" height="847" viewBox="0 0 1086 847" aria-hidden="true">
    <rect width="1086" height="847" fill="#1b1b1b"/>
    <rect x="730" width="356" height="847" fill="#1a1a1a"/>
    <polygon points="0,0 730,0 730,405 688,535 401,535 0,95" fill="#f2e43f"/>
    <polygon points="0,95 401,535 348,535 0,142" fill="#e4262b"/>
  </svg>

  <section class="panel panel-left">
    <h2 class="about-title">ABOUT US</h2>
    <div class="keys-photo" role="img" aria-label="Black and white photo of a pile of antique keys"></div>
    <p class="about-text">
      The Vaults of KDW is a "real<br>
      life" escape game in which<br>
      teams of 2-10 are locked in a<br>
      deeply thematic room and given 1<br>
      hour to find their way out. By<br>
      searching for clues, solving puzzles, and<br>
      discovering the secrets each of our rooms<br>
      have to offer, teams will attempt to beat the clock in<br>
      this creative new form of entertainment.
    </p>
    <div class="hours">
      <p>Our current business hours are:</p>
      <p class="hl">Monday through Thursday</p>
      <p>from 4:00 pm - 10:30 pm</p>
      <p><span class="hl">Fridays from 3:00 pm - 11:30 pm</span></p>
      <p>and <span class="hl">Saturdays</span> from 1:00 pm 11:30 pm</p>
      <div class="divider"></div>
      <p class="closed">We are closed on Sundays, but if you would like to book u can contact us by phone at <span class="yellow">(555)-304-8812</span> or by email at <span class="yellow">info@thevaultsofkdw.com</span>, and we will do what we can to accomodate you.</p>
    </div>
    <p class="sign-off">WE LOOK FORWARD TO<br>HEARING FROM YOU!</p>
  </section>

  <section class="panel panel-middle">
    <h1 class="brand-title">THE VAULTS<br>OF KDW</h1>
    <div class="title-rule"></div>
    <p class="tagline">Live Escape Games</p>
    <div class="map-area" role="img" aria-label="Street map showing the location of The Vaults of KDW"></div>
    <p class="address">
      <svg width="11" height="13" viewBox="0 0 11 13"><path d="M5.5 0C2.5 0 .5 2.2.5 5c0 3.3 5 8 5 8s5-4.7 5-8C10.5 2.2 8.5 0 5.5 0z" fill="#161616"/><circle cx="5.5" cy="5" r="1.8" fill="#f2e43f"/></svg>1418 Harlow Avenue<br>Suite 204, Ridgeford TX
    </p>
    <div class="wordmark wordmark-middle"><span class="mark"></span>THE VAULTS of KDW</div>
    <p class="phone">
      <svg width="20" height="20" viewBox="0 0 20 20" style="vertical-align:-2px;margin-right:4px"><circle cx="10" cy="10" r="9" fill="none" stroke="#f2e43f" stroke-width="1.6"/><path d="M7 5.5l1.6 2.3-1 1.2c.6 1.3 1.6 2.3 2.9 2.9l1.2-1 2.3 1.6-.9 1.8c-3.6-.3-6.6-3.3-6.9-6.9z" fill="#f2e43f"/></svg>(555) 304-8812
    </p>
    <div class="contact contact-middle">
      <p><svg width="12" height="9" viewBox="0 0 12 9"><rect x=".5" y=".5" width="11" height="8" fill="none" stroke="#f2e43f"/><path d="M.5.5L6 5l5.5-4.5" fill="none" stroke="#f2e43f"/></svg>info@thevaultsofkdw.com</p>
      <p><svg width="11" height="11" viewBox="0 0 12 12"><circle cx="6" cy="6" r="5.3" fill="none" stroke="#f2e43f"/><path d="M.7 6h10.6M6 .7c-2.8 3-2.8 7.6 0 10.6M6 .7c2.8 3 2.8 7.6 0 10.6" fill="none" stroke="#f2e43f"/></svg>www.thevaultsofkdw.com</p>
    </div>
  </section>

  <section class="panel panel-right">
    <div class="wordmark wordmark-right"><span class="mark"></span>THE VAULTS of KDW</div>
    <p class="subtitle">Live Escape Games</p>
    <div class="contact contact-right">
      <p><svg width="12" height="9" viewBox="0 0 12 9"><rect x=".5" y=".5" width="11" height="8" fill="none" stroke="#f2e43f"/><path d="M.5.5L6 5l5.5-4.5" fill="none" stroke="#f2e43f"/></svg>info@thevaultsofkdw.com</p>
      <p><svg width="11" height="11" viewBox="0 0 12 12"><circle cx="6" cy="6" r="5.3" fill="none" stroke="#f2e43f"/><path d="M.7 6h10.6M6 .7c-2.8 3-2.8 7.6 0 10.6M6 .7c2.8 3 2.8 7.6 0 10.6" fill="none" stroke="#f2e43f"/></svg>www.thevaultsofkdw.com</p>
    </div>
    <div class="door-photo" role="img" aria-label="Photo of a dark room with a door opening onto bright light"></div>
  </section>
</main>
</body>
</html>
```